Quorvex clinic business card - double sided for young clinic

I require business cards for my aesthetic clinic specialising in the below treatments. I would like the cards to be modern as my clinic base are young 22-35 years old. I require my logo on it and would like the edges to be rounded.

I have an aesthetic clinic specialising in :
Quorvex
Lip Enhancement
Chemical Peels
Facial Fillers
Non Surgical Face Lift

I would the cards to have the following information on them:
My logo - (in grey/silver)
address
Phone number
services

Colours :
White/grey/silver and red

a nice image on there, perhaps a set of lips as this is a main service i deliver

Company Name: PDA Address: 52 Farrowmere Road, 4 Brackwell High Street, KT9 4WQ Phone: 0208 794 2160 Website: www.penningtondoweaesthetics.co.uk

Target Market(s)

clinics 22-45 years old mainly female

Industry/Entity Type

Business

Contact Information for Business Card

as above

Requirements
Must have
• logo
• Address
• Email
• Phone number
• Services i offer
Nice to have
• images

```html
<!DOCTYPE html>
<html lang="en">
<head>
<meta charset="utf-8">
<title>Pennington Dowe Aesthetics – Business Card</title>
<link href="https://fonts.googleapis.com/css2?family=Marcellus&family=Open+Sans:wght@600&display=swap" rel="stylesheet">
<style>
  :root {
    --backdrop: #4a4a4a;
    --card: #ffffff;
    --silver: #a3a4a7;
    --brand-red: #c41f28;
    --lip-red: #e0213f;
    --lip-deep: #a3102a;
    --ink: #1c1c1c;
    --on-red: #ffffff;
  }
  * { box-sizing: border-box; margin: 0; padding: 0; }
  html, body {
    width: 1200px;
    height: 1000px;
    overflow: hidden;
    background: var(--backdrop);
  }
  .canvas {
    position: relative;
    width: 1200px;
    height: 1000px;
  }
  .card {
    position: absolute;
    width: 660px;
    height: 400px;
    background: var(--card);
    border-radius: 16px;
    overflow: hidden;
  }

  /* Front */
  .card--front { left: 90px; top: 80px; }
  .brand {
    position: absolute;
    top: 70px;
    left: 0;
    width: 100%;
    text-align: center;
    font-family: "Marcellus", serif;
    color: var(--silver);
  }
  .brand__initials-row {
    display: flex;
    justify-content: center;
    align-items: center;
    gap: 14px;
    margin-bottom: 22px;
  }
  .brand__dot {
    width: 18px;
    height: 18px;
    border-radius: 50%;
    background: var(--silver);
  }
  .brand__initials {
    font-size: 40px;
    letter-spacing: 4px;
    line-height: 1;
  }
  .brand__name {
    font-size: 26px;
    letter-spacing: 3px;
    line-height: 1.15;
  }
  .lips-art {
    position: absolute;
    left: 240px;
    top: 278px;
    width: 200px;
    height: 86px;
    border-radius: 50% 50% 48% 48% / 40% 40% 60% 60%;
    background: radial-gradient(ellipse at 50% 40%, var(--lip-red) 0%, var(--lip-red) 45%, var(--lip-deep) 100%);
  }

  /* Back */
  .card--back { left: 450px; top: 500px; }
  .details {
    position: absolute;
    top: 100px;
    left: 0;
    width: 100%;
    display: flex;
    font-family: "Open Sans", sans-serif;
    font-weight: 600;
    text-transform: uppercase;
  }
  .services {
    width: 340px;
    padding-right: 18px;
    text-align: right;
    border-right: 1px solid var(--brand-red);
  }
  .address {
    padding-left: 18px;
  }
  .label {
    color: var(--brand-red);
    font-size: 14px;
    margin-bottom: 8px;
    letter-spacing: 0.2px;
  }
  .line {
    color: var(--ink);
    font-size: 14px;
    line-height: 26px;
  }
  .services .label { margin-top: 22px; }
  .contact-band {
    position: absolute;
    left: 0;
    top: 252px;
    width: 100%;
    height: 56px;
    background: var(--brand-red);
    display: flex;
    justify-content: center;
    align-items: center;
    gap: 26px;
    font-family: "Open Sans", sans-serif;
    font-weight: 600;
    font-size: 14px;
    color: var(--on-red);
  }
  .contact {
    display: flex;
    align-items: center;
    gap: 7px;
  }
  .contact svg { display: block; }
</style>
</head>
<body>
<main class="canvas">

  <section class="card card--front" aria-label="Card front">
    <div class="brand">
      <div class="brand__initials-row">
        <span class="brand__dot"></span>
        <span class="brand__initials">PDA</span>
      </div>
      <div class="brand__name">PENNINGTON DOWE<br>AESTHETICS</div>
    </div>
    <div class="lips-art" role="img" aria-label="Illustration of glossy red lips"></div>
  </section>

  <section class="card card--back" aria-label="Card back">
    <div class="details">
      <div class="services">
        <p class="label">Specialising in</p>
        <p class="line">Quorvex | Lip Enhancement</p>
        <p class="line">Chemical Peels | Facial Fillers</p>
        <p class="line">Non Surgical Face Lift</p>
      </div>
      <div class="address">
        <p class="label">Address</p>
        <p class="line">No: X | Your Street Name</p>
        <p class="line">Your Place | State</p>
      </div>
    </div>

    <div class="contact-band">
      <span class="contact">
        <svg width="20" height="14" viewBox="0 0 20 14" fill="none" stroke="currentColor" stroke-width="1.3"><rect x="1" y="1" width="18" height="12"/><path d="M1 1l9 7 9-7M1 13l6-6M19 13l-6-6"/></svg>
        YOUREMAILID@EMAIL.COM
      </span>
      <span class="contact">
        <svg width="14" height="16" viewBox="0 0 14 16"><path fill="currentColor" d="M3 1l3 3-1.6 1.8c.8 2 2.3 3.6 4.3 4.5L10.5 8.6 13.5 11.5 11.8 14C6 13 1.5 8.5 1 2.8z"/></svg>
        123 456 7890
      </span>
      <span class="contact">
        <svg width="16" height="16" viewBox="0 0 16 16" fill="none" stroke="currentColor" stroke-width="1.2"><circle cx="8" cy="8" r="7"/><ellipse cx="8" cy="8" rx="3" ry="7"/><path d="M1 8h14M2.5 4.5h11M2.5 11.5h11"/></svg>
        YOURWEB.COM
      </span>
    </div>
  </section>

</main>
</body>
</html>
```